Need simple and modern looking business card with all my information on one side and logo on the other side
Info :
Company name - VELMAR CONSTRUCTION LLC
Company addres- 418 harbor 87th. Dunmoor park ny 10352
Email- velmarllc@tridomail.Com
Company phone number 555-318-6094
Cell number- 555-742-0583
Web site - velmarllc.Com
My name Gerald tomasino

Target Market(s)

Construction , home improvement, remodeling

Industry/Entity Type

Construction

Contact Information for Business Card

It has to be moder but at the same time simple

Font styles to use
Sans Serif

Colors
0255a3
ffffff
000000
f78f20
b1b1b1
9d9d9d
1b1b1b
33a6d7
ec1f27

Requirements
Must have
• My logo on one side maybe with a some kind of background on the other side all my information
Nice to have
• Some kind of background pictures provided by you .PLEASE HAVE ACCOUNT WITH PIXELVAULT WILL NOT PAY ANY EXTRA FEES .
Should not have
• Any kind of hamer, nails,screws, helmets itp. Please do not copy the other designs come up with something new.

```html
<!DOCTYPE html>
<html lang="en">
<head>
<meta charset="utf-8">
<title>Velmar Construction LLC – Business Card</title>
<link rel="stylesheet" href="https://fonts.googleapis.com/css2?family=Open+Sans:wght@400;600&family=Orbitron:wght@500&display=swap">
<style>
  :root {
    --backdrop: #e4e4e4;
    --card-black: #000000;
    --card-dark: #1b1b1b;
    --card-white: #f7f7f6;
    --ink: #1b1b1b;
    --white: #ffffff;
    --orange: #f78f20;
    --navy: #0255a3;
    --sky: #33a6d7;
    --red: #ec1f27;
    --grey-light: #b1b1b1;
    --grey-mid: #9d9d9d;
  }
  * { box-sizing: border-box; margin: 0; padding: 0; }
  html, body { width: 1200px; height: 900px; overflow: hidden; }
  body {
    background: var(--backdrop);
    font-family: "Open Sans", Arial, sans-serif;
    color: var(--ink);
    position: relative;
  }
  .card {
    position: absolute;
    left: 250px;
    width: 700px;
    height: 400px;
    overflow: hidden;
    box-shadow: 0 6px 18px rgba(0,0,0,0.18);
  }
  /* Front side */
  .card-front {
    top: 33px;
    background: var(--card-black);
  }
  .card-front .streaks { position: absolute; inset: 0; }
  .front-mark {
    position: absolute;
    left: 0; right: 0; top: 168px;
    display: flex;
    align-items: center;
    justify-content: center;
    gap: 16px;
  }
  .front-mark .mark-square {
    width: 26px; height: 26px;
    background: var(--orange);
  }
  .front-mark .company-name {
    font-family: "Open Sans", Arial, sans-serif;
    font-weight: 600;
    font-size: 40px;
    letter-spacing: 3px;
    color: var(--white);
  }
  /* Back side */
  .card-back {
    top: 467px;
    background: var(--card-white);
  }
  .holder-name {
    position: absolute;
    left: 120px; top: 62px;
    font-family: "Orbitron", "Open Sans", sans-serif;
    font-weight: 500;
    font-size: 27px;
    letter-spacing: 3px;
    color: var(--orange);
    text-transform: uppercase;
  }
  .contact-list {
    position: absolute;
    left: 120px; top: 122px;
    list-style: none;
  }
  .contact-item {
    display: flex;
    align-items: center;
    gap: 14px;
    font-size: 19px;
    line-height: 1.3;
    margin-bottom: 26px;
  }
  .contact-item svg { width: 22px; height: 22px; flex: none; }
  .back-mark {
    position: absolute;
    right: 40px; bottom: 40px;
    display: flex;
    align-items: center;
    gap: 8px;
  }
  .back-mark .mark-square { width: 12px; height: 12px; background: var(--orange); }
  .back-mark .company-name {
    font-weight: 600;
    font-size: 15px;
    letter-spacing: 1px;
    color: var(--ink);
  }
</style>
</head>
<body>

<section class="card card-front" aria-label="Card front">
  <svg class="streaks" viewBox="0 0 700 400" aria-hidden="true">
    <defs>
      <linearGradient id="streak" x1="0" y1="0" x2="0" y2="1">
        <stop offset="0" stop-color="#555" stop-opacity="0"/>
        <stop offset="0.5" stop-color="#6a6a6a" stop-opacity="0.7"/>
        <stop offset="1" stop-color="#555" stop-opacity="0"/>
      </linearGradient>
    </defs>
    <polygon points="150,0 162,0 70,230 66,230" fill="url(#streak)"/>
    <polygon points="350,250 356,250 300,400 292,400" fill="url(#streak)"/>
    <polygon points="560,170 566,170 520,330 514,330" fill="url(#streak)"/>
    <polygon points="670,120 676,120 630,300 624,300" fill="url(#streak)"/>
    <rect x="380" y="30" width="200" height="290" fill="none" stroke="var(--card-dark)" stroke-width="3"/>
  </svg>
  <div class="front-mark">
    <span class="mark-square"></span>
    <span class="company-name">VELMAR CONSTRUCTION LLC</span>
  </div>
</section>

<section class="card card-back" aria-label="Card back">
  <h1 class="holder-name">Gerald Tomasino</h1>
  <ul class="contact-list">
    <li class="contact-item">
      <svg viewBox="0 0 24 24" aria-hidden="true"><path d="M12 2a7 7 0 0 0-7 7c0 5 7 13 7 13s7-8 7-13a7 7 0 0 0-7-7zm0 9.5a2.5 2.5 0 1 1 0-5 2.5 2.5 0 0 1 0 5z" fill="none" stroke="var(--navy)" stroke-width="1.6"/></svg>
      <span>418 Harbor 87th.<br>Dunmoor Park NY 10352</span>
    </li>
    <li class="contact-item">
      <svg viewBox="0 0 24 24" aria-hidden="true"><rect x="3" y="6" width="18" height="12" fill="none" stroke="var(--red)" stroke-width="1.6"/><path d="M3 6l9 7 9-7" fill="none" stroke="var(--red)" stroke-width="1.6"/></svg>
      <span>velmarllc@tridomail.com</span>
    </li>
    <li class="contact-item">
      <svg viewBox="0 0 24 24" aria-hidden="true"><path d="M6 3l3 4-2 2c1 3 4 6 7 7l2-2 4 3-2 3C10 20 4 14 3 5z" fill="none" stroke="var(--sky)" stroke-width="1.6" stroke-linejoin="round"/></svg>
      <span>555-318-6094<br>555-742-0583</span>
    </li>
    <li class="contact-item">
      <svg viewBox="0 0 24 24" aria-hidden="true"><g fill="none" stroke="var(--red)" stroke-width="1.6"><circle cx="12" cy="12" r="9"/><ellipse cx="12" cy="12" rx="4" ry="9"/><path d="M3 12h18M5 7h14M5 17h14"/></g></svg>
      <span>velmarllc.com</span>
    </li>
  </ul>
  <div class="back-mark">
    <span class="mark-square"></span>
    <span class="company-name">VELMAR CONSTRUCTION LLC</span>
  </div>
</section>

</body>
</html>
```